Storm Restoration Contractor needs a professional letterhead design

Looking for a professional letterhead design. Not looking for your cheapo MS Word standard ones that are readily available. Dont want it to be cookie cutter look like ones readily available online. We just recently changed our logo and want to freshen up all our documents. Our company handles restoring a property back to a pre-loss condition after a storm damages it. For example, wind, hail, flood, fire losses.

Target Market(s)

Property Owners, Homeowners, Property Owners, Commercial Property Owners, Property Management Companies

Industry/Entity Type

Construction Company

Requirements
Must have
• Professional, Use 1 of 2 logo options
• Storm Restoration, Roofing, Siding, Windows

```html
<!DOCTYPE html>
<html lang="en">
<head>
<meta charset="utf-8">
<title>Stormline Exteriors Letterhead</title>
<link rel="stylesheet" href="https://fonts.googleapis.com/css2?family=Open+Sans:wght@600;700&display=swap">
<style>
  :root {
    --backdrop: #e6e7e9;
    --paper: #ffffff;
    --brand-blue: #1273c0;
    --footer-text: #ffffff;
  }
  html, body {
    margin: 0;
    padding: 0;
    width: 1200px;
    height: 1200px;
    overflow: hidden;
    background: var(--backdrop);
  }
  .canvas {
    position: relative;
    width: 1200px;
    height: 1200px;
  }
  .letterhead {
    position: absolute;
    left: 194px;
    top: 40px;
    width: 812px;
    height: 1120px;
    background: var(--paper);
    font-family: "Open Sans", sans-serif;
  }
  .brand {
    position: absolute;
    top: 50px;
    left: 0;
    right: 0;
    display: flex;
    justify-content: center;
    align-items: center;
    gap: 20px;
  }
  .brand-dot {
    width: 88px;
    height: 88px;
    border-radius: 50%;
    background: var(--brand-blue);
    flex: none;
  }
  .brand-name {
    color: var(--brand-blue);
    font-weight: 700;
    font-size: 34px;
    line-height: 1.08;
    letter-spacing: 1.5px;
    text-transform: uppercase;
  }
  .brand-name .line { display: block; }
  .contact-band {
    position: absolute;
    left: 0;
    right: 0;
    top: 1068px;
    height: 46px;
    background: var(--brand-blue);
    color: var(--footer-text);
    display: flex;
    flex-direction: column;
    justify-content: center;
    align-items: center;
    font-weight: 600;
    font-size: 12.5px;
    line-height: 16px;
    letter-spacing: -0.2px;
  }
  .contact-line span + span { margin-left: 10px; }
</style>
</head>
<body>
<div class="canvas">
  <div class="letterhead">
    <header class="brand">
      <div class="brand-dot"></div>
      <div class="brand-name"><span class="line">Stormline</span><span class="line">Exteriors</span></div>
    </header>
    <footer class="contact-band">
      <div class="contact-line">215 Harbor View Rd Ste 120, Fairview, MD 20999</div>
      <div class="contact-line"><span>P: 301-555-0142</span><span>F: 301-555-0178</span><span>W: www.stormlineexteriors.com</span></div>
    </footer>
  </div>
</div>
</body>
</html>
```